New Web-Page Design Required

We need a new or initial web design for our page vorlan-grid.com. We provide products & services around infrastructure products. We have two products at the moment, but another 2 in the pipeline.
We want to have the following page structure (and part of the project is to design the 7 pages):
- Home
- Products
-One page per product
- Service
- Support
- About
- Contact (Email form)
The start page should include the following information:
- Twitter / Linkedin Links
- Telephone / Email or in general contact details
- News
- Maybe a link-box, where we can highlight/showcase things
- Link to our support portal, quite prominent
- Testimonials
It would be nice if the product pages would have a image header, where we can put up a screenshot or something. Links to datasheet and videos of the product would be nice as well.
We like the "big banner in the middle" designs, like these two Joomla examples. No need to copy them, it should just give you an idea.
http://www.pelmorthemes.com/itempreview/185
http://www.pelmorthemes.com/content/asj42/index.php
Budget for images available, so please use placeholders or ask us for specific photos/images, if you need them for your design.
Target Market(s)
Business-2-Business, Decision makers and Technical Leads
Industry/Entity Type
News
Look and feel

```html
<!DOCTYPE html>
<html lang="en">
<head>
<meta charset="utf-8">
<title>Our Service – Vorlan-Grid</title>
<link href="https://fonts.googleapis.com/css2?family=Jost:wght@300;400;500&family=Arimo:wght@400&display=swap" rel="stylesheet">
<style>
:root{
  --teal:#12aeb8;
  --teal-dark:#0aa3ad;
  --ink:#3b3f45;
  --text:#8a8d92;
  --white:#ffffff;
  --paper:#f3f3f5;
  --tweet-bg:#373d47;
  --footer-bg:#30363f;
  --icon:#8b8e93;
}
*{box-sizing:border-box;margin:0;padding:0}
html,body{width:1200px;height:1088px;overflow:hidden}
body{position:relative;background:var(--white);font-family:"Arimo",Arial,sans-serif;color:var(--text)}
.site-header{position:absolute;left:0;top:0;width:1200px;height:78px;background:linear-gradient(#f4f4f5,#fff)}
.brand{position:absolute;left:187px;top:20px;display:flex;align-items:center;gap:8px;font-family:"Jost",sans-serif;font-weight:500;font-size:26px;color:#4a4e54;letter-spacing:-.3px}
.brand-dot{width:34px;height:34px;border-radius:50%;background:var(--teal-dark)}
.main-nav{position:absolute;right:187px;top:32px;display:flex;font-family:"Jost",sans-serif;font-size:14px;color:var(--ink);letter-spacing:.2px}
.main-nav a{color:inherit;text-decoration:none}
.main-nav a.is-current{color:var(--teal)}
.main-nav .sep{color:#c7c9cc;margin:0 11px;font-size:15px}
.page-banner{position:absolute;left:0;top:78px;width:1200px;height:113px;background:linear-gradient(100deg,#2ebcc2 0%,#1fb4bb 55%,#12aab4 100%)}
.breadcrumb{position:absolute;left:187px;top:43px;width:390px;height:31px;padding-left:12px;display:flex;align-items:center;gap:4px;font-size:10px;color:#2f6e73;background:linear-gradient(90deg,rgba(30,150,160,.55),rgba(30,150,160,0));border-left:1px solid rgba(255,255,255,.25)}
.breadcrumb strong{font-family:"Jost",sans-serif;font-weight:500;font-size:13px;color:var(--white);letter-spacing:.3px}
.service{position:absolute;left:0;top:191px;width:1200px;height:374px}
h2{font-family:"Jost",sans-serif;font-weight:400;font-size:17px;color:var(--ink);letter-spacing:.6px}
.service h2{position:absolute;left:187px;top:30px}
.service-copy{position:absolute;left:187px;top:82px;width:420px;font-size:9.4px;line-height:16px;letter-spacing:.3px}
.service-copy p{margin-bottom:18px}
.steps{list-style:none;margin-top:20px}
.steps li{position:relative;padding-left:14px;margin-bottom:8px}
.steps li::before{content:"›";position:absolute;left:0;top:-1px;color:#4a4e54;font-size:12px}
.service-photo{position:absolute;left:651px;top:85px;width:361px;height:164px;border:1px solid #e6e6e8;padding:5px;background:var(--white)}
.service-photo div{width:100%;height:100%;background:linear-gradient(90deg,#0e4e58 0%,#2d8c93 45%,#7fb7b9 75%,#3f6e77 100%)}
.why{position:absolute;left:0;top:565px;width:1200px;height:325px;background:var(--paper)}
.skills-visual{position:absolute;left:187px;top:25px;width:278px;height:278px;border-radius:50%;background:radial-gradient(circle,#1b2d3a 0%,#1b2d3a 30%,#8aa6b4 55%,#c9dbe4 75%,rgba(243,243,245,0) 72%)}
.why h2{position:absolute;left:600px;top:38px}
.why-copy{position:absolute;left:600px;top:92px;width:415px;font-size:9.4px;line-height:16px;letter-spacing:.3px}
.why-copy p{margin-bottom:18px}
.points{list-style:none;margin-top:18px}
.points li{position:relative;padding-left:18px;margin-bottom:8px}
.points li::before{content:"";position:absolute;left:0;top:6px;width:4px;height:4px;background:#4a4e54}
.tweets{position:absolute;left:0;top:890px;width:1200px;height:123px;background:var(--tweet-bg);text-align:center;font-family:"Jost",sans-serif;color:var(--white)}
.tweets-title{position:absolute;left:0;right:0;top:21px;display:flex;justify-content:center;align-items:center;gap:12px;font-size:18px;font-weight:400;letter-spacing:.4px}
.tweets-title span.mark{width:22px;height:22px;border-radius:50%;background:var(--white)}
.tweet-line{position:absolute;left:0;right:0;top:56px;font-size:17px;font-weight:300}
.tweet-line .hl{color:var(--teal)}
.view-media{position:absolute;left:0;right:0;top:81px;display:flex;justify-content:center;align-items:center;gap:6px;font-size:17px;font-weight:300}
.view-media svg{display:block}
.site-footer{position:absolute;left:0;top:1013px;width:1200px;height:75px;background:var(--footer-bg);font-size:10px;color:var(--white)}
.footer-contact{position:absolute;left:187px;top:22px;line-height:18px;letter-spacing:.3px}
.footer-contact .hl{color:var(--teal)}
.social{position:absolute;left:837px;top:23px;display:flex;gap:4px;list-style:none}
.social li{width:26px;height:26px;border-radius:50%;background:var(--icon)}
</style>
</head>
<body>
<header class="site-header">
  <div class="brand"><span class="brand-dot"></span>vorlan·grid</div>
  <nav class="main-nav">
    <a href="#">Home</a><span class="sep">/</span>
    <a href="#">Our Products</a><span class="sep">/</span>
    <a href="#" class="is-current">Our Service</a><span class="sep">/</span>
    <a href="#">Support</a><span class="sep">/</span>
    <a href="#">About Us</a><span class="sep">/</span>
    <a href="#">Contact Us</a>
  </nav>
</header>

<section class="page-banner">
  <div class="breadcrumb">Your here : Home &gt; <strong>Our Service</strong></div>
</section>

<section class="service">
  <h2>Our Service</h2>
  <div class="service-copy">
    <p>Installation &amp; Professional Services can be provided by us or competent partners. In any case, you will get very experienced software consultants, who can fix every issue.</p>
    <p>Our service offerings include everything from infrastructure consulting, installation of the software and training how to use it and to get the best out of it. We can help you at any stage of your project or we can even do the full implementation for you. Usually our projects will follow the following process and stages:</p>
    <ul class="steps">
      <li>Infrastructure Design (Cluster vs. Non Cluster, Security, Uptime considerations)</li>
      <li>Installation (n.Metric, VCD/C, Database, LDAP Connectivity)</li>
      <li>Configuration (Performance Reviews, Push-Notification Configuration)</li>
      <li>Post-Installation Testing</li>
      <li>Training</li>
    </ul>
  </div>
  <figure class="service-photo"><div role="img" aria-label="Photo of a consultant touching a glowing digital world map interface"></div></figure>
</section>

<section class="why">
  <div class="skills-visual" role="img" aria-label="Skills illustration: concentric coloured rings around a dark circle labelled Skills"></div>
  <h2>Why Choose Us</h2>
  <div class="why-copy">
    <p>Lorem ipsum dolor sit amet, consectetur adipisicing elit, sed do eiusmod tempor incididunt ut labore et dolore magna aliqua. Ut enim ad minim veniam, quis nostrud exercitation ullamco laboris nisi ut aliquip ex ea commodo consequat. Duis aute irure dolor in reprehenderit in voluptate velit esse cillum dolore eu fugiat nulla pariatur cupidatat non proident.</p>
    <p>Excepteur sint occaecat cupidatat non proident, sunt in culpa qui officia deserunt mollit anim id est laborum regenaret lomastica.</p>
    <ul class="points">
      <li>Vestibulum vulputate orci et justo fermentum lacus imperdiet.</li>
      <li>Duis euismod vulputate urna, quis dignissim justo laoreet id.</li>
      <li>Nulla sit amet nulla vel nisl tincidunt ornare eu nec ligula.</li>
    </ul>
  </div>
</section>

<section class="tweets">
  <div class="tweets-title"><span class="mark"></span>Tweets</div>
  <p class="tweet-line"><span class="hl">Vorlan-Grid</span> @vorlangrid <span class="hl">n.Metric Video:</span> vid.lk/R4tQm8XwZa</p>
  <p class="view-media"><svg width="16" height="11" viewBox="0 0 16 11"><rect width="16" height="11" fill="#12aeb8"/><path d="M6 2.5 L11 5.5 L6 8.5 Z" fill="#373d47"/></svg>View media</p>
</section>

<footer class="site-footer">
  <div class="footer-contact">
    <div>Info@vorlan-grid.com</div>
    <div>Copyright © 2013 <span class="hl">Vorlan-Grid</span></div>
  </div>
  <ul class="social" aria-label="Social links">
    <li></li><li></li><li></li><li></li><li></li><li></li>
  </ul>
</footer>
</body>
</html>
```